Pharmacy and Travel Clinic Leaflet

We are an established pharmacy and gift shop which also runs a travel and vaccination clinic. We have had the same leaflet for a couple of years and would like to refresh it for the following reasons:
We have rebranded our travel and vaccination clinic as Fellgate Journey Clinic with its own dedicated website (www.fellgatejourneyclinic.co.uk).
We have made changes to our prices that need to be reflected in the new leaflet.

The original leaflet was a little information heavy as the service was new and we would like the new leaflet to be more visually appealing with the pharmacy side highlighting our services and using the colours of our logo (purple and green) and the vaccination side using the colours of our travel clinic logo (navy blue, light blue, red and white). Logo's are attached in a variety of formats as I have no idea what is most useful.

I will upload some images that may assist with the design, as well as updated text for the pharmacy leaflet and the new prices and text required for the vaccination side. I do not expect all of the images to be used.

The leaflet is to be two-sided, which we will print in A3 and possibly enlarge to use on a large A-Board.

I would like to receive the files in format(s) that can be sent to a printers and also added to our website to display our prices.

I have attached a copy of our existing leaflet for reference.

If any information requires clarification or there are files that you need to improve the design then please let me know and I will try to sort that out.

P.S. The font we usually use now is Orkney

I have an extra requirement if this is possible. On the pharmacy services side of the leaflet I would like the tagline Providing QRS services at the bottom right of the leaflet. It can go on the bottom left if necessary. It doesn't need to be large. It needs to be in the black font (Arial or Helvetica) with the QRS logo in blue. I have attached a link to the QRS logo website and files are now uploaded to give you an idea of what we need.
The Providing QRS services and logo need to be exactly as shown in the uploads. The QRS do not allow their logo to be used creatively.
https://www.example-qrs-health.org/qrsidentity/identity-guidelines/service-branding/

Thanks for all the submissions. They were very good but I had to choose one.

Target Market(s)

All ages from young students through to pensioners.

Industry/Entity Type

Pharmacy

Font styles to use
Sans Serif

Colors
9bcb3c
6c459b
ec1f27
0255a3
ffffff

Requirements
Must have
• Leaflet needs to be professional yet still be bold enough to stand out.
• Premium look using colours stated in brief. Colours differ for pharmacy side and travel clinic side. Please don't mix pharmacy and travel colours
Nice to have
• Please use the logos and tie the scheme in with those colours. Where the prices of vaccines are listed they need to be clear
• The Providing QRS services line and logo need to be exactly as shown in the uploads. The QRS do not allow their logo to be used creatively.
Should not have
• Must not be too informal. No comedy fonts

```html
<!DOCTYPE html>
<html lang="en">
<head>
<meta charset="utf-8">
<title>Brookfield Chemist &amp; Fellgate Journey Clinic Leaflet</title>
<link href="https://fonts.googleapis.com/css2?family=Jost:wght@400;500;600;700&family=Tinos:wght@700&display=swap" rel="stylesheet">
<style>
:root{
  --stage:#3f3f3f;
  --paper:#ffffff;
  --green:#9bcb3c;
  --purple:#6c459b;
  --purple-dark:#4f2d86;
  --navy:#0255a3;
  --navy-dark:#0b4a9a;
  --sky:#3fa9f5;
  --red:#ec1f27;
  --ink:#1d1d1d;
}
*{margin:0;padding:0;box-sizing:border-box}
html,body{width:1200px;height:1200px;overflow:hidden;background:var(--stage)}
body{position:relative;font-family:"Jost",Arial,sans-serif;color:var(--ink)}
.leaflet{position:absolute;top:140px;height:846px;background:var(--paper);overflow:hidden;box-shadow:0 6px 18px rgba(0,0,0,.45)}
.pharmacy{left:30px;width:556px}
.travel{left:604px;width:564px}
.abs{position:absolute}

/* pharmacy side */
.hero-photo{left:0;top:0;width:556px;height:396px;background:linear-gradient(160deg,#5b5b5e 0%,#2f3a6b 35%,#c9c9cf 70%,#e7e7ea 100%)}
.brand-box{left:22px;top:0;width:160px;height:111px;background:var(--paper);border-radius:0 0 8px 8px;display:flex;flex-direction:column;align-items:center;justify-content:center;gap:6px;text-align:center;color:var(--purple);font-weight:500;font-size:14px;line-height:1.1}
.brand-box .mark{width:30px;height:30px;background:var(--purple)}
.services-heading{left:0;top:420px;width:556px;text-align:center;font-family:"Tinos","Times New Roman",serif;font-weight:700;font-size:19.5px;line-height:23px;color:var(--purple-dark);text-transform:uppercase}
.service-list{left:41px;top:482px;list-style:none;font-size:9.6px;line-height:15.4px}
.service-list li,.vaccine-list li,.malaria-list li,.extra-list li{display:flex;align-items:center;gap:7px}
.tick{flex:none;width:7px;height:7px}
.side-photo{left:323px;width:200px}
.photo-cold{top:483px;height:139px;background:linear-gradient(135deg,#b9a792,#e8e2d8 55%,#d7c3a8)}
.photo-quit{top:629px;height:142px;background:linear-gradient(135deg,#3b73b9,#d9b89e 50%,#eef2f8)}
.address{left:41px;top:656px;font-weight:700;font-size:13.5px;color:var(--purple-dark)}
.hours-label{left:42px;background:var(--green);color:#fff;font-size:12px;padding:1px 10px;line-height:16px}
.hours-time{left:52px;font-size:12px;color:var(--purple-dark)}
.footer{left:0;top:782px;width:100%;height:52px;display:flex;align-items:center;color:#fff}
.pharmacy .footer{background:var(--green)}
.travel .footer{background:var(--navy-dark);top:784px;height:54px}
.footer .phone{display:flex;align-items:center;gap:14px;font-family:"Tinos","Times New Roman",serif;font-weight:700;font-size:29px}
.footer .divider{width:1px;height:38px;background:rgba(255,255,255,.8);margin:0 18px}
.footer .web{display:flex;align-items:center;gap:10px;font-size:14.5px}
.footer .web b{font-weight:600}

/* travel side */
.scenes{left:0;top:0;width:564px;height:844px}
.clinic-brand{left:16px;top:40px;display:flex;align-items:center;gap:8px;color:var(--red);font-weight:600;font-size:16px;line-height:1.1;width:190px}
.clinic-brand .dot{flex:none;width:26px;height:26px;border-radius:50%;background:var(--sky)}
.tab{background:var(--navy-dark);color:#fff;font-weight:700;font-size:15px;padding:0 0 0 22px;height:29px;line-height:29px;letter-spacing:.2px;white-space:nowrap}
.tab-vaccines{left:0;top:404px;width:176px}
.tab-malaria{left:0;top:604px;width:164px}
.tab-extra{left:308px;top:572px;width:232px;padding-left:12px;font-size:15px}
.vaccine-list,.malaria-list,.extra-list{list-style:none;font-weight:600;font-size:8.4px;color:#111}
.vaccine-list{left:22px;top:440px;width:200px;line-height:14.4px}
.vaccine-list li .price,.extra-list li .price{margin-left:auto;color:var(--red);font-weight:700}
.malaria-list{left:24px;top:641px;line-height:11px}
.malaria-list li{align-items:flex-start;margin-bottom:6px}
.malaria-list .tick{margin-top:2px}
.extra-list{left:322px;top:607px;width:216px;line-height:15.4px}
.notes{left:33px;top:714px;color:var(--navy);font-size:9px;line-height:10px}
.notes p:first-child{margin-bottom:6px}
.notes small{font-size:7.4px;display:block;line-height:9.4px}
</style>
</head>
<body>

<section class="leaflet pharmacy">
  <div class="abs hero-photo" role="img" aria-label="Photo of a family with colds sitting in bed with tissues"></div>
  <div class="abs brand-box">
    <span class="mark"></span>
    <span>BROOKFIELD CHEMIST<br>PHARMACY &amp; GIFTS</span>
  </div>

  <h1 class="abs services-heading">Long-established independent pharmacy<br>offering a wide range of services including:</h1>

  <ul class="abs service-list">
    <li><svg class="tick" viewBox="0 0 10 10"><circle cx="5" cy="5" r="5" fill="#6c459b"/><path d="M2.6 5.2l1.6 1.6 3.2-3.4" stroke="#fff" stroke-width="1.4" fill="none"/></svg>Free prescription collection &amp; delivery service</li>
    <li><svg class="tick" viewBox="0 0 10 10"><circle cx="5" cy="5" r="5" fill="#6c459b"/><path d="M2.6 5.2l1.6 1.6 3.2-3.4" stroke="#fff" stroke-width="1.4" fill="none"/></svg>Large stocks, multiple suppliers &amp; efficient, personal service</li>
    <li><svg class="tick" viewBox="0 0 10 10"><circle cx="5" cy="5" r="5" fill="#6c459b"/><path d="M2.6 5.2l1.6 1.6 3.2-3.4" stroke="#fff" stroke-width="1.4" fill="none"/></svg>Experienced staff working with cutting edge automation</li>
    <li><svg class="tick" viewBox="0 0 10 10"><circle cx="5" cy="5" r="5" fill="#6c459b"/><path d="M2.6 5.2l1.6 1.6 3.2-3.4" stroke="#fff" stroke-width="1.4" fill="none"/></svg>Cholesterol Testing</li>
    <li><svg class="tick" viewBox="0 0 10 10"><circle cx="5" cy="5" r="5" fill="#6c459b"/><path d="M2.6 5.2l1.6 1.6 3.2-3.4" stroke="#fff" stroke-width="1.4" fill="none"/></svg>Quit Smoking Service</li>
    <li><svg class="tick" viewBox="0 0 10 10"><circle cx="5" cy="5" r="5" fill="#6c459b"/><path d="M2.6 5.2l1.6 1.6 3.2-3.4" stroke="#fff" stroke-width="1.4" fill="none"/></svg>Minor Ailments Scheme</li>
    <li><svg class="tick" viewBox="0 0 10 10"><circle cx="5" cy="5" r="5" fill="#6c459b"/><path d="M2.6 5.2l1.6 1.6 3.2-3.4" stroke="#fff" stroke-width="1.4" fill="none"/></svg>Mobility Aids</li>
    <li><svg class="tick" viewBox="0 0 10 10"><circle cx="5" cy="5" r="5" fill="#6c459b"/><path d="M2.6 5.2l1.6 1.6 3.2-3.4" stroke="#fff" stroke-width="1.4" fill="none"/></svg>Free Text Notification Service</li>
    <li><svg class="tick" viewBox="0 0 10 10"><circle cx="5" cy="5" r="5" fill="#6c459b"/><path d="M2.6 5.2l1.6 1.6 3.2-3.4" stroke="#fff" stroke-width="1.4" fill="none"/></svg>Seasonal Flu Vaccination</li>
    <li><svg class="tick" viewBox="0 0 10 10"><circle cx="5" cy="5" r="5" fill="#6c459b"/><path d="M2.6 5.2l1.6 1.6 3.2-3.4" stroke="#fff" stroke-width="1.4" fill="none"/></svg>Private vaccinations for individuals &amp; groups</li>
  </ul>

  <div class="abs side-photo photo-cold" role="img" aria-label="Photo of a woman with a cold resting under a blanket"></div>
  <div class="abs side-photo photo-quit" role="img" aria-label="Photo of hands snapping a cigarette in half"></div>

  <p class="abs address">14 Market Row, Ashwick. AB1 2CD</p>
  <p class="abs hours-label" style="top:680px">Monday to Friday:</p>
  <p class="abs hours-time" style="top:703px">8.30am – 6.00pm</p>
  <p class="abs hours-label" style="top:724px">Saturday:</p>
  <p class="abs hours-time" style="top:747px">8.30am – 4.00pm</p>

  <div class="abs footer" style="padding-left:48px">
    <span class="phone"><svg width="22" height="22" viewBox="0 0 24 24"><path fill="#fff" d="M6.6 10.8c1.4 2.8 3.8 5.1 6.6 6.6l2.2-2.2c.3-.3.7-.4 1-.2 1.1.4 2.3.6 3.6.6.6 0 1 .4 1 1V20c0 .6-.4 1-1 1C10.6 21 3 13.4 3 4c0-.6.4-1 1-1h3.5c.6 0 1 .4 1 1 0 1.3.2 2.5.6 3.6.1.3 0 .7-.2 1l-2.3 2.2z"/></svg>01632 960418</span>
    <span class="divider"></span>
    <span class="web"><svg width="14" height="14" viewBox="0 0 20 20" fill="none" stroke="#fff" stroke-width="1.5"><circle cx="10" cy="10" r="8.5"/><ellipse cx="10" cy="10" rx="3.8" ry="8.5"/><path d="M1.5 10h17M3 5.5h14M3 14.5h14"/></svg><span>www.<b>brookfieldchemist</b>.com</span></span>
  </div>
</section>

<section class="leaflet travel">
  <svg class="abs scenes" viewBox="0 0 705 1055" preserveAspectRatio="none">
    <defs>
      <linearGradient id="g-lagoon" x1="0" y1="0" x2="0" y2="1"><stop offset="0" stop-color="#2f6fc4"/><stop offset=".45" stop-color="#9cc6ea"/><stop offset=".6" stop-color="#3fb7c6"/><stop offset="1" stop-color="#d8c59a"/></linearGradient>
      <linearGradient id="g-beach" x1="0" y1="0" x2="0" y2="1"><stop offset="0" stop-color="#2a7bd0"/><stop offset=".5" stop-color="#4a9a3c"/><stop offset=".7" stop-color="#49c2d0"/><stop offset="1" stop-color="#efe6d2"/></linearGradient>
      <radialGradient id="g-insect" cx=".45" cy=".55" r=".6"><stop offset="0" stop-color="#a5502c"/><stop offset=".5" stop-color="#3a2014"/><stop offset="1" stop-color="#0d0906"/></radialGradient>
    </defs>
    <polygon points="367,0 705,0 705,245 410,467 257,125" fill="url(#g-lagoon)" role="img" aria-label="Photo of a longtail boat on a turquoise tropical bay beside limestone cliffs"/>
    <polygon points="245,137 420,312 260,493 75,315" fill="url(#g-beach)" role="img" aria-label="Photo of a palm tree and hammock over a tropical beach"/>
    <polygon points="435,315 610,490 435,670 265,493" fill="url(#g-insect)" role="img" aria-label="Close-up photo of a mosquito on skin"/>
  </svg>

  <div class="abs clinic-brand"><span class="dot"></span>Fellgate Journey Clinic</div>

  <h2 class="abs tab tab-vaccines">TRAVEL VACCINES</h2>
  <ul class="abs vaccine-list">
    <li><svg class="tick" viewBox="0 0 10 10"><circle cx="5" cy="5" r="5" fill="#0b4a9a"/><path d="M2.6 5.2l1.6 1.6 3.2-3.4" stroke="#fff" stroke-width="1.4" fill="none"/></svg>Cholera<span class="price">£25</span></li>
    <li><svg class="tick" viewBox="0 0 10 10"><circle cx="5" cy="5" r="5" fill="#0b4a9a"/><path d="M2.6 5.2l1.6 1.6 3.2-3.4" stroke="#fff" stroke-width="1.4" fill="none"/></svg>Diphtheria Tetanus and Polio<span class="price">£30</span></li>
    <li><svg class="tick" viewBox="0 0 10 10"><circle cx="5" cy="5" r="5" fill="#0b4a9a"/><path d="M2.6 5.2l1.6 1.6 3.2-3.4" stroke="#fff" stroke-width="1.4" fill="none"/></svg>Hepatitis A<span class="price">£40</span></li>
    <li><svg class="tick" viewBox="0 0 10 10"><circle cx="5" cy="5" r="5" fill="#0b4a9a"/><path d="M2.6 5.2l1.6 1.6 3.2-3.4" stroke="#fff" stroke-width="1.4" fill="none"/></svg>Hepatitis B<span class="price">£40</span></li>
    <li><svg class="tick" viewBox="0 0 10 10"><circle cx="5" cy="5" r="5" fill="#0b4a9a"/><path d="M2.6 5.2l1.6 1.6 3.2-3.4" stroke="#fff" stroke-width="1.4" fill="none"/></svg>Hepatitis A &amp; B (combined)<span class="price">£70</span></li>
    <li><svg class="tick" viewBox="0 0 10 10"><circle cx="5" cy="5" r="5" fill="#0b4a9a"/><path d="M2.6 5.2l1.6 1.6 3.2-3.4" stroke="#fff" stroke-width="1.4" fill="none"/></svg>Hepatitis A &amp; Typhoid (combined)<span class="price">£70</span></li>
    <li><svg class="tick" viewBox="0 0 10 10"><circle cx="5" cy="5" r="5" fill="#0b4a9a"/><path d="M2.6 5.2l1.6 1.6 3.2-3.4" stroke="#fff" stroke-width="1.4" fill="none"/></svg>Japanese Encephalitis<span class="price">£85</span></li>
    <li><svg class="tick" viewBox="0 0 10 10"><circle cx="5" cy="5" r="5" fill="#0b4a9a"/><path d="M2.6 5.2l1.6 1.6 3.2-3.4" stroke="#fff" stroke-width="1.4" fill="none"/></svg>Meningitis ACWY<span class="price">£50</span></li>
    <li><svg class="tick" viewBox="0 0 10 10"><circle cx="5" cy="5" r="5" fill="#0b4a9a"/><path d="M2.6 5.2l1.6 1.6 3.2-3.4" stroke="#fff" stroke-width="1.4" fill="none"/></svg>Rabies<span class="price">£60</span></li>
    <li><svg class="tick" viewBox="0 0 10 10"><circle cx="5" cy="5" r="5" fill="#0b4a9a"/><path d="M2.6 5.2l1.6 1.6 3.2-3.4" stroke="#fff" stroke-width="1.4" fill="none"/></svg>Tick Borne Encephalitis<span class="price">£60</span></li>
    <li><svg class="tick" viewBox="0 0 10 10"><circle cx="5" cy="5" r="5" fill="#0b4a9a"/><path d="M2.6 5.2l1.6 1.6 3.2-3.4" stroke="#fff" stroke-width="1.4" fill="none"/></svg>Typhoid<span class="price">£35</span></li>
  </ul>

  <h2 class="abs tab tab-malaria">ANTIMALARIALS</h2>
  <ul class="abs malaria-list">
    <li><svg class="tick" viewBox="0 0 10 10"><circle cx="5" cy="5" r="5" fill="#0b4a9a"/><path d="M2.6 5.2l1.6 1.6 3.2-3.4" stroke="#fff" stroke-width="1.4" fill="none"/></svg><span>Generic Atovaquone/Proguanil tablets -<br>£2 per tablet</span></li>
    <li><svg class="tick" viewBox="0 0 10 10"><circle cx="5" cy="5" r="5" fill="#0b4a9a"/><path d="M2.6 5.2l1.6 1.6 3.2-3.4" stroke="#fff" stroke-width="1.4" fill="none"/></svg><span>Doxycycline 100mg 50p per capsule</span></li>
  </ul>

  <h2 class="abs tab tab-extra">We also vaccinate against:</h2>
  <ul class="abs extra-list">
    <li><svg class="tick" viewBox="0 0 10 10"><circle cx="5" cy="5" r="5" fill="#0b4a9a"/><path d="M2.6 5.2l1.6 1.6 3.2-3.4" stroke="#fff" stroke-width="1.4" fill="none"/></svg>Chickenpox<span class="price">£60</span></li>
    <li><svg class="tick" viewBox="0 0 10 10"><circle cx="5" cy="5" r="5" fill="#0b4a9a"/><path d="M2.6 5.2l1.6 1.6 3.2-3.4" stroke="#fff" stroke-width="1.4" fill="none"/></svg>Measles Mumps &amp; Rubella (MMR)<span class="price">£40</span></li>
    <li><svg class="tick" viewBox="0 0 10 10"><circle cx="5" cy="5" r="5" fill="#0b4a9a"/><path d="M2.6 5.2l1.6 1.6 3.2-3.4" stroke="#fff" stroke-width="1.4" fill="none"/></svg>Meningitis B<span class="price">£110</span></li>
    <li><svg class="tick" viewBox="0 0 10 10"><circle cx="5" cy="5" r="5" fill="#0b4a9a"/><path d="M2.6 5.2l1.6 1.6 3.2-3.4" stroke="#fff" stroke-width="1.4" fill="none"/></svg>Shingles<span class="price">£150</span></li>
    <li><svg class="tick" viewBox="0 0 10 10"><circle cx="5" cy="5" r="5" fill="#0b4a9a"/><path d="M2.6 5.2l1.6 1.6 3.2-3.4" stroke="#fff" stroke-width="1.4" fill="none"/></svg>Human Papilloma Virus (HPV)<span class="price">£150</span></li>
  </ul>

  <div class="abs notes">
    <p>*Prices are per dose &amp; more than one dose of vaccine may be needed</p>
    <small>**The availability and price of the above may vary. During shortages<br>wholesale prices can rise and we will inform you of any price changes</small>
  </div>

  <div class="abs footer" style="padding-left:42px">
    <span class="phone"><svg width="22" height="22" viewBox="0 0 24 24"><path fill="#fff" d="M6.6 10.8c1.4 2.8 3.8 5.1 6.6 6.6l2.2-2.2c.3-.3.7-.4 1-.2 1.1.4 2.3.6 3.6.6.6 0 1 .4 1 1V20c0 .6-.4 1-1 1C10.6 21 3 13.4 3 4c0-.6.4-1 1-1h3.5c.6 0 1 .4 1 1 0 1.3.2 2.5.6 3.6.1.3 0 .7-.2 1l-2.3 2.2z"/></svg>01632 960418</span>
    <span class="divider"></span>
    <span class="web" style="font-size:13.5px"><svg width="14" height="14" viewBox="0 0 20 20" fill="none" stroke="#fff" stroke-width="1.5"><circle cx="10" cy="10" r="8.5"/><ellipse cx="10" cy="10" rx="3.8" ry="8.5"/><path d="M1.5 10h17M3 5.5h14M3 14.5h14"/></svg><span>www.<b>fellgatejourneyclinic</b>.co.uk</span></span>
  </div>
</section>

</body>
</html>
```